Geschäftspapiere für Unternehmen aus Not- und Sicherheitsbeleuchtungsbranche
Zielgruppe
Wir sind ein Unternehmen der Not- und Sicherheitsbeleuchtungsbranche und arbeiten vornehmlich mit dem deutschen Elektrogroßhandel zusammen.
Aufgabenstellung
WIr möchten nicht nur Schreibblöcke drucken, wir benötigen die Vorlage auch als Word-Datei für Geschäftsbriefe.
Orientierung und Farbwahl gemäß unserer Website. Im Anhang finden Sie bereits das aktuelle Briefdesign. Dieses verbraucht jedoch zu viel Platz und liegt uns nicht als Word vor. Die Daten können übernommen werden, ergänzt muss noch die UST-ID werden: DE718206359

```html
<!DOCTYPE html>
<html lang="de">
<head>
<meta charset="utf-8">
<title>Veltrona Licht GmbH – Briefbogen</title>
<link rel="stylesheet" href="https://fonts.googleapis.com/css2?family=Montserrat:wght@400;500;700&display=swap">
<style>
  :root {
    --magenta: #a8005e;
    --slate: #5f6873;
    --ink: #1d1d1f;
    --mark: #ebebed;
    --backdrop: #e3e7e8;
    --paper: #ffffff;
  }
  * { box-sizing: border-box; margin: 0; padding: 0; }
  html, body {
    width: 1092px; height: 1200px; overflow: hidden;
    background: var(--backdrop);
    font-family: "Montserrat", Arial, sans-serif;
    color: var(--ink);
  }
  .letterhead {
    position: absolute; left: 146px; top: 34px;
    width: 800px; height: 1132px;
    background: var(--paper);
    box-shadow: 0 6px 18px rgba(0,0,0,.12);
    overflow: hidden;
  }
  .sender-line {
    position: absolute; left: 92px; top: 168px;
    font-size: 8.5px; letter-spacing: .1px;
    padding-bottom: 3px;
    border-bottom: 1.5px solid var(--magenta);
  }
  .fold-mark {
    position: absolute; left: 0; width: 22px;
    border-top: 1px solid #c9c9cc;
  }
  .fold-mark--top { top: 400px; }
  .fold-mark--punch { top: 566px; }
  .fold-mark--bottom { top: 732px; }

  .brand {
    position: absolute; right: 64px; top: 120px;
    display: flex; align-items: center; gap: 10px;
  }
  .brand__square { width: 22px; height: 22px; background: var(--magenta); }
  .brand__name {
    font-size: 24px; font-weight: 500; letter-spacing: 3px;
    color: var(--slate);
  }
  .contact-block {
    position: absolute; right: 64px; top: 176px;
    width: 146px;
    border-left: 2px solid var(--slate);
    padding-left: 12px;
    font-size: 10.5px; line-height: 1.45;
  }
  .contact-block__company { color: var(--magenta); font-weight: 700; }
  .contact-row { display: flex; align-items: center; gap: 6px; }
  .icon { width: 9px; height: 9px; flex: none; fill: var(--magenta); }

  .backdrop-name {
    position: absolute; left: 0; right: 0; top: 470px;
    text-align: center;
    font-size: 96px; font-weight: 400; letter-spacing: 14px;
    color: var(--mark);
  }

  .footer {
    position: absolute; left: 0; bottom: 0; width: 800px; height: 150px;
  }
  .footer__bands { position: absolute; left: 0; bottom: 0; }
  .footer__col {
    position: absolute; top: 14px;
    font-size: 9px; line-height: 1.4;
  }
  .footer__col strong { font-weight: 700; }
  .footer__col .label { color: var(--magenta); font-weight: 700; }
  .footer__col--company { left: 96px; }
  .footer__col--board { left: 200px; top: 30px; }
  .footer__col--contact { left: 320px; top: 46px; }
  .footer__col--register { left: 452px; top: 60px; }
  .footer__col--bank { left: 574px; top: 60px; }
</style>
</head>
<body>
  <main class="letterhead">
    <p class="sender-line">Veltrona Licht GmbH · Lindenweg 7 · D-83210 Seehofen</p>

    <span class="fold-mark fold-mark--top"></span>
    <span class="fold-mark fold-mark--punch"></span>
    <span class="fold-mark fold-mark--bottom"></span>

    <div class="brand">
      <span class="brand__square"></span>
      <span class="brand__name">VELTRONA</span>
    </div>

    <address class="contact-block">
      <div class="contact-block__company">Veltrona Licht GmbH</div>
      <div>Lindenweg 7</div>
      <div>D-83210 Seehofen</div>
      <div class="contact-row">
        <svg class="icon" viewBox="0 0 10 10"><path d="M2 0.5 L4 2.5 L3 3.8 Q4.2 6 6.2 7 L7.5 6 L9.5 8 L8 9.5 Q3.5 9.5 0.5 2 Z"/></svg>08651 73204 19
      </div>
      <div class="contact-row">
        <svg class="icon" viewBox="0 0 10 10"><rect x="0" y="2" width="10" height="6.5"/></svg>info@veltrona-licht.de
      </div>
      <div class="contact-row">
        <svg class="icon" viewBox="0 0 10 10"><circle cx="5" cy="5" r="4.6"/></svg>www.veltrona-licht.de
      </div>
    </address>

    <div class="backdrop-name" aria-hidden="true">VELTRONA</div>

    <footer class="footer">
      <svg class="footer__bands" width="800" height="150" viewBox="0 0 800 150">
        <polygon points="0,84 300,136 290,150 0,150" fill="var(--magenta)" style="fill:#a8005e"/>
        <polygon points="0,100 280,150 0,150" fill="#a8005e"/>
        <polygon points="320,150 330,120 800,130 800,150" fill="#5f6873"/>
      </svg>

      <div class="footer__col footer__col--company">
        <strong>Veltrona Licht GmbH</strong><br>Lindenweg 7<br>D-83210 Seehofen
      </div>
      <div class="footer__col footer__col--board">
        <span class="label">Geschäftsführer</span><br>Moritz Kelbing<br>Managing Director
      </div>
      <div class="footer__col footer__col--contact">
        <div class="contact-row"><svg class="icon" viewBox="0 0 10 10"><path d="M2 0.5 L4 2.5 L3 3.8 Q4.2 6 6.2 7 L7.5 6 L9.5 8 L8 9.5 Q3.5 9.5 0.5 2 Z"/></svg>08651 73204 19</div>
        <div class="contact-row"><svg class="icon" viewBox="0 0 10 10"><rect x="0" y="2" width="10" height="6.5"/></svg>info@veltrona-licht.de</div>
        <div class="contact-row"><svg class="icon" viewBox="0 0 10 10"><circle cx="5" cy="5" r="4.6"/></svg>www.veltrona-licht.de</div>
      </div>
      <div class="footer__col footer__col--register">
        Amtsgericht Seehofen<br>HRB 40927<br>USt-ID DE718206359
      </div>
      <div class="footer__col footer__col--bank">
        Bankverbindung Sparkasse Seehofen Nord<br>BLZ 720 431 60<br>IBAN: DE42 7204 3160 0051 2973 04<br>BIC: BYLADEM1SHF
      </div>
    </footer>
  </main>
</body>
</html>
```